Letterhead Design

I would like 2 different letterheads. One with each logo I have attached. Business info:
Prairie Claims Billing, LLC
3478 N Birch
Linden Vale, NE 68792
(866) 555-0143

```html
<!DOCTYPE html>
<html lang="en">
<head>
<meta charset="utf-8">
<title>Prairie Claims Billing — Letterhead</title>
<link rel="stylesheet" href="https://fonts.googleapis.com/css2?family=Open+Sans:wght@400;600&family=Tinos:wght@400;700&display=swap">
<style>
  :root {
    --backdrop: #e4e4e2;
    --paper: #ffffff;
    --teal: #1b9aa6;
    --ink: #2b2b2b;
    --ink-soft: #555555;
    --sign-tone: #ececec;
  }
  * { box-sizing: border-box; margin: 0; padding: 0; }
  html, body { width: 1200px; height: 1091px; overflow: hidden; }
  body {
    background: var(--backdrop);
    display: flex;
    align-items: center;
    justify-content: center;
  }
  .letterhead {
    position: relative;
    width: 730px;
    height: 1033px;
    background: var(--paper);
    box-shadow: 0 4px 18px rgba(0,0,0,0.12);
    border-right: 6px solid var(--teal);
    display: flex;
    flex-direction: column;
  }
  .letterhead__header {
    padding: 54px 58px 0 58px;
    display: flex;
    flex-direction: column;
    align-items: flex-end;
  }
  .brand {
    display: flex;
    align-items: center;
    gap: 12px;
    font-family: "Open Sans", sans-serif;
    font-weight: 600;
    font-size: 20px;
    color: var(--teal);
  }
  .brand__mark {
    width: 28px; height: 28px;
    background: var(--teal);
    border-radius: 50%;
  }
  .recipient {
    margin-top: 34px;
    text-align: right;
    font-family: "Tinos", serif;
    color: var(--ink);
  }
  .recipient__name { font-size: 24px; letter-spacing: 0.5px; }
  .recipient__role { font-size: 18px; margin-top: 2px; }
  .letter-body {
    padding: 40px 58px 0 58px;
    font-family: "Open Sans", sans-serif;
    color: var(--ink-soft);
  }
  .letter-body__title {
    font-size: 10px;
    font-weight: 400;
    letter-spacing: 0.5px;
    margin-bottom: 10px;
  }
  .letter-body p {
    font-size: 12.5px;
    line-height: 1.55;
    text-indent: 36px;
    margin-bottom: 22px;
  }
  .signature {
    margin: 20px 0 0 120px;
    width: 150px;
    height: 60px;
    background: var(--sign-tone);
    border-radius: 4px;
  }
  .letterhead__footer {
    margin-top: auto;
    height: 46px;
    background: var(--teal);
    color: #ffffff;
    font-family: "Tinos", serif;
    font-size: 16px;
    display: flex;
    align-items: center;
    justify-content: space-between;
    padding: 0 40px;
    white-space: nowrap;
  }
</style>
</head>
<body>
  <main class="letterhead">
    <header class="letterhead__header">
      <div class="brand">
        <span class="brand__mark"></span>
        <span class="brand__name">Prairie Claims Billing, LLC</span>
      </div>
      <div class="recipient">
        <div class="recipient__name">Mr. LOREM IPSUM</div>
        <div class="recipient__role">Designation, Company Name</div>
      </div>
    </header>

    <section class="letter-body">
      <h2 class="letter-body__title">LOREM IPSUM DUMMY TEXT</h2>
      <p>Lorem Ipsum is simply dummy text of the printing and typesetting industry. Lorem Ipsum has been the industry's standard dummy text ever since the 1500s, when an unknown printer took a galley of type and scrambled it to make a type specimen book. It has survived not only five centuries, but also the leap into electronic typesetting, remaining essentially unchanged. It was popularised in the 1960s with the release of Quillmark sheets containing Lorem Ipsum passages, and more recently with desktop publishing software like Folio Layout including versions of Lorem Ipsum.</p>
      <p>Lorem Ipsum is simply dummy text of the printing and typesetting industry. Lorem Ipsum has been the industry's standard dummy text ever since the 1500s, when an unknown printer took a galley of type and scrambled it to make a type specimen book. It has survived not only five centuries, but also the leap into electronic typesetting, remaining essentially unchanged. It was popularised in the 1960s with the release of Quillmark sheets containing Lorem Ipsum passages, and more recently with desktop publishing software like Folio Layout including versions of Lorem Ipsum.</p>
      <p>Lorem Ipsum is simply dummy text of the printing and typesetting industry. Lorem Ipsum has been the industry's standard dummy text ever since the 1500s, when an unknown printer took a galley of type and scrambled it to make a type specimen book. It has survived not only five centuries, but also the leap into electronic typesetting, remaining essentially unchanged. It was popularised in the 1960s with the release of Quillmark sheets containing Lorem Ipsum passages, and more recently with desktop publishing software like Folio Layout including versions of Lorem Ipsum.</p>
      <div class="signature" role="img" aria-label="Handwritten signature"></div>
    </section>

    <footer class="letterhead__footer">
      <span class="footer__company">Prairie Claims Billing, LLC</span>
      <span class="footer__phone">(866) 555-0143</span>
      <span class="footer__address">3478 N Birch, Linden Vale, NE 68792</span>
    </footer>
  </main>
</body>
</html>
```